Marrowby Lane School bookmark

We need a vertical card (DL 99x210 mm) that will be put inside books at a primary school for children to make comments about the books. Text at the top:
Marrowby Lane School (and logo)
What did you think of this book?

Text at the bottom:
Pass it on!

Words in repeated pattern around the edge: funny sad exciting mysterious fantastic boring enthralling interesting

It should be in interesting bright colours with a white or pale background as children will write on the cards

The card should be double sided with the same design on each side

Industry/Entity Type

School

```html
<!DOCTYPE html>
<html lang="en">
<head>
<meta charset="utf-8">
<title>Marrowby Lane School – Book Comment Bookmark</title>
<link rel="stylesheet" href="https://fonts.googleapis.com/css2?family=Archivo+Black&family=Roboto+Condensed:wght@300;400;700&display=swap">
<style>
  :root {
    --backdrop: #474747;
    --paper: #ffffff;
    --school-red: #c1272d;
    --pink-pale: #f7c5d6;
    --pink: #ef8db5;
    --lime: #c9d62c;
    --sky: #6cb5e4;
    --blue: #4aa3df;
    --sage: #b7d0a2;
    --mint: #a9dbb5;
    --aqua-pale: #a9ded8;
    --lilac: #cca2d2;
    --orange: #f39200;
    --sun: #fbc02d;
    --green: #7fbf5a;
    --teal: #1db5a4;
    --tick-yellow: #f5e400;
    --rule: #333333;
  }
  * { margin: 0; padding: 0; box-sizing: border-box; }
  html, body {
    width: 1200px;
    height: 2400px;
    overflow: hidden;
    background: var(--backdrop);
  }
  .bookmark {
    position: absolute;
    left: 50px;
    top: 100px;
    width: 1100px;
    height: 2200px;
    background: var(--paper);
    overflow: hidden;
  }
  .bookmark-art {
    position: absolute;
    inset: 0;
    width: 1100px;
    height: 2200px;
  }
  .band { fill: var(--school-red); }
  .paper { fill: var(--paper); }
  .crest-disc { fill: var(--school-red); stroke: #7d1418; stroke-width: 6; }
  .school-name {
    font-family: "Roboto Condensed", sans-serif;
    font-weight: 700;
    font-size: 34px;
    fill: var(--paper);
    letter-spacing: 1px;
  }
  .word { font-family: "Roboto Condensed", sans-serif; }
  .w-light { font-weight: 300; }
  .w-reg { font-weight: 400; }
  .w-bold { font-weight: 700; }
  .c-pink-pale { fill: var(--pink-pale); }
  .c-pink { fill: var(--pink); }
  .c-lime { fill: var(--lime); }
  .c-sky { fill: var(--sky); }
  .c-blue { fill: var(--blue); }
  .c-sage { fill: var(--sage); }
  .c-mint { fill: var(--mint); }
  .c-aqua { fill: var(--aqua-pale); }
  .c-lilac { fill: var(--lilac); }
  .c-orange { fill: var(--orange); }
  .c-sun { fill: var(--sun); }
  .c-green { fill: var(--green); }
  .c-red { fill: var(--school-red); }
  .check-box { fill: none; stroke: var(--school-red); stroke-width: 7; }
  .check-tick { fill: none; stroke: var(--school-red); stroke-width: 10; stroke-linecap: round; stroke-linejoin: round; }
  .write-line { stroke: var(--rule); stroke-width: 3; stroke-dasharray: 2 5; }
  .pass-pill { fill: var(--teal); stroke: var(--paper); stroke-width: 6; }
  .pass-shadow { fill: #1b1b1b; opacity: 0.35; }
  .pass-text {
    font-family: "Archivo Black", sans-serif;
    font-size: 54px;
    fill: var(--paper);
    letter-spacing: 2px;
  }
  .pass-tick { fill: none; stroke: var(--tick-yellow); stroke-width: 8; stroke-linecap: round; stroke-linejoin: round; }
  .web-address {
    font-family: "Roboto Condensed", sans-serif;
    font-weight: 700;
    font-size: 42px;
    fill: var(--paper);
    letter-spacing: 1px;
  }
  .web-highlight { fill: var(--sun); }
</style>
</head>
<body>
<main class="bookmark">
  <svg class="bookmark-art" viewBox="0 0 1100 2200" xmlns="http://www.w3.org/2000/svg">
    <!-- header band with curved rise behind the crest -->
    <rect class="band" x="0" y="0" width="1100" height="260"/>
    <path class="paper" d="M0,228 C280,228 330,112 550,108 C770,112 820,228 1100,228 V400 H0 Z"/>

    <!-- school crest placeholder and name -->
    <g class="crest">
      <circle class="crest-disc" cx="550" cy="300" r="152"/>
      <text class="school-name" x="550" y="294" text-anchor="middle">MARROWBY LANE</text>
      <text class="school-name" x="550" y="336" text-anchor="middle">SCHOOL</text>
    </g>

    <!-- word cloud -->
    <g class="word-cloud">
      <text class="word w-bold c-pink-pale" x="82" y="605" font-size="140" textLength="482" lengthAdjust="spacingAndGlyphs">FANTASTIC</text>
      <text class="word w-reg c-orange" font-size="30" textLength="70" lengthAdjust="spacingAndGlyphs" transform="translate(612,598) rotate(-90)">SAD</text>
      <text class="word w-reg c-lime" x="646" y="588" font-size="130" textLength="308" lengthAdjust="spacingAndGlyphs">FUNNY</text>

      <text class="word w-bold c-sky" font-size="100" textLength="274" lengthAdjust="spacingAndGlyphs" transform="translate(164,916) rotate(-90)">FUNNY</text>

      <text class="word w-bold c-red" x="215" y="769" font-size="186" textLength="440" lengthAdjust="spacingAndGlyphs">WHAT</text>
      <text class="word w-bold c-red" x="215" y="830" font-size="42" textLength="470" lengthAdjust="spacingAndGlyphs">DID YOU THINK OF THIS</text>
      <text class="word w-bold c-red" x="215" y="1015" font-size="262" textLength="490" lengthAdjust="spacingAndGlyphs">BOOK</text>
      <text class="word w-bold c-red" x="712" y="1015" font-size="400" textLength="150" lengthAdjust="spacingAndGlyphs">?</text>

      <text class="word w-reg c-sage" font-size="48" textLength="143" lengthAdjust="spacingAndGlyphs" transform="translate(143,1076) rotate(-90)">BORING</text>
      <text class="word w-bold c-green" font-size="28" textLength="143" lengthAdjust="spacingAndGlyphs" transform="translate(188,1076) rotate(-90)">ENTHRALLING</text>

      <text class="word w-reg c-lime" font-size="48" textLength="256" lengthAdjust="spacingAndGlyphs" transform="translate(878,820) rotate(90)">EXCITING</text>
      <text class="word w-bold c-mint" font-size="90" textLength="482" lengthAdjust="spacingAndGlyphs" transform="translate(990,1076) rotate(-90)">INTERESTING</text>

      <text class="word w-bold c-sky" x="226" y="1121" font-size="96" textLength="256" lengthAdjust="spacingAndGlyphs">FUNNY</text>
      <text class="word w-bold c-aqua" x="512" y="1072" font-size="52" textLength="267" lengthAdjust="spacingAndGlyphs">INTERESTING</text>
      <text class="word w-reg c-lilac" x="512" y="1148" font-size="80" textLength="369" lengthAdjust="spacingAndGlyphs">MYSTERIOUS</text>
      <text class="word w-bold c-orange" x="908" y="1138" font-size="50" textLength="66" lengthAdjust="spacingAndGlyphs">SAD</text>

      <text class="word w-reg c-orange" x="113" y="1230" font-size="94" textLength="373" lengthAdjust="spacingAndGlyphs">FANTASTIC</text>
      <text class="word w-reg c-blue" x="512" y="1203" font-size="38" textLength="195" lengthAdjust="spacingAndGlyphs">ENTHRALLING</text>
      <text class="word w-reg c-red" font-size="20" textLength="29" lengthAdjust="spacingAndGlyphs" transform="translate(736,1203) rotate(-90)">SAD</text>
      <text class="word w-bold c-blue" x="752" y="1203" font-size="46" textLength="222" lengthAdjust="spacingAndGlyphs">FANTASTIC</text>

      <g class="checkbox">
        <rect class="check-box" x="126" y="1252" width="66" height="66"/>
        <path class="check-tick" d="M140,1280 L158,1304 L196,1244"/>
      </g>
      <text class="word w-bold c-sun" x="215" y="1312" font-size="92" textLength="464" lengthAdjust="spacingAndGlyphs">MYSTERIOUS</text>
      <text class="word w-reg c-pink" x="703" y="1287" font-size="92" textLength="283" lengthAdjust="spacingAndGlyphs">BORING</text>
    </g>

    <!-- comment lines -->
    <g class="comment-lines">
      <line class="write-line" x1="205" y1="1404" x2="892" y2="1404"/>
      <line class="write-line" x1="205" y1="1494" x2="892" y2="1494"/>
      <line class="write-line" x1="205" y1="1584" x2="892" y2="1584"/>
      <line class="write-line" x1="205" y1="1674" x2="892" y2="1674"/>
      <line class="write-line" x1="205" y1="1764" x2="892" y2="1764"/>
    </g>

    <!-- footer band -->
    <path class="band" d="M0,1972 C300,2012 800,2012 1100,1972 V2200 H0 Z"/>

    <!-- pass it on button -->
    <g class="pass-it-on">
      <rect class="pass-shadow" x="272" y="1882" width="670" height="86" rx="43"/>
      <rect class="pass-pill" x="265" y="1872" width="670" height="86" rx="43"/>
      <text class="pass-text" x="560" y="1935" text-anchor="middle">PASS IT ON!</text>
      <path class="pass-tick" d="M826,1912 L840,1930 L868,1890"/>
    </g>

    <!-- web address -->
    <text class="web-address" x="550" y="2112" text-anchor="middle">WWW.<tspan class="web-highlight">MARROWBYLANE</tspan>.EASTBURY.SCH.UK</text>
  </svg>
</main>
</body>
</html>
```